The Duchess of Nestware is an online store specialising in all things for the home Bathroom, Kitchen,

I need a business card designed that is professional and elegant, yet not conservative. We will be wanting to brand the entire business and will have videos made where we will be interacting with the product, testing the products and basically creating an online interactive community for all those people interested in all things to do with the Home and the activities that take place in and around the home.

Target Market(s)

30-65yr old Men and Women who LOVE their Home and see it as their primary place of Happiness, their sanctuary!

Industry/Entity Type

Business

Contact Information for Business Card

www.duchessofnestware.example The Duchess Of Nestware-PO Box 58316, Marlow Flats, Auckland. NEW ZEALAND. info@duchessofnestware.example
Love your Home! Corinne Dale-Petrakou

Font styles to use
Decorative
Script

Colors
9bcb3b
33b8a4
85cae6
b7a5cd
eda3c7
e667a6
d2a4cc
fdf9cf
fee18a

Requirements
Must have
• Attractive colours. Must feel Elegant, yet simple. A font that is rounded without sharp edges. Organic feel to the card, something raw with texture.
Nice to have
• I like the logo deign that I gave in the photos, something feminine, but fun.
Should not have
• I dont like sharp edges, or linear design. I like organic, flowing, fractal type design. Something that looks beautiful in form when you look at it.

```html
<!DOCTYPE html>
<html lang="en">
<head>
<meta charset="utf-8">
<title>The Duchess of Nestware – Business Card</title>
<link rel="stylesheet" href="https://fonts.googleapis.com/css2?family=Quicksand:wght@500;600;700&family=Dancing+Script:wght@500&display=swap">
<style>
  :root {
    --backdrop: #1a1b1b;
    --card-front: #f8dc9c;
    --card-back: #ffffff;
    --brand-blue: #3c9cc8;
    --brand-pink: #e62b93;
  }
  * { box-sizing: border-box; margin: 0; padding: 0; }
  html, body {
    width: 1200px;
    height: 1000px;
    overflow: hidden;
    background: var(--backdrop);
  }
  .canvas {
    position: relative;
    width: 1200px;
    height: 1000px;
    font-family: "Quicksand", sans-serif;
  }
  .card {
    position: absolute;
    left: 280px;
    width: 640px;
    height: 360px;
    border-radius: 22px;
  }
  .card--front {
    top: 110px;
    background: var(--card-front);
  }
  .card--back {
    top: 530px;
    background: var(--card-back);
  }
  .wordmark {
    position: absolute;
    left: 0;
    right: 0;
    top: 90px;
    text-align: center;
    color: var(--brand-blue);
    font-weight: 700;
    font-size: 46px;
    line-height: 1.15;
  }
  .address-rule {
    position: absolute;
    left: 90px;
    right: 90px;
    top: 238px;
    height: 0;
    border-top: 1.5px solid var(--brand-blue);
  }
  .address {
    position: absolute;
    left: 0;
    right: 0;
    top: 250px;
    text-align: center;
    color: var(--brand-blue);
    font-weight: 500;
    font-size: 17px;
  }
  .brand-dot {
    position: absolute;
    left: 296px;
    top: 62px;
    width: 48px;
    height: 48px;
    border-radius: 50%;
    background: var(--brand-pink);
  }
  .person-name {
    position: absolute;
    left: 0;
    right: 0;
    top: 124px;
    text-align: center;
    color: var(--brand-blue);
    font-weight: 600;
    font-size: 38px;
  }
  .tagline {
    position: absolute;
    left: 0;
    right: 0;
    top: 172px;
    text-align: center;
    color: var(--brand-blue);
    font-family: "Dancing Script", cursive;
    font-weight: 500;
    font-size: 34px;
  }
  .contact-line {
    position: absolute;
    left: 44px;
    bottom: 40px;
    color: var(--brand-blue);
    font-weight: 500;
    font-size: 17px;
  }
</style>
</head>
<body>
  <main class="canvas">
    <section class="card card--front" aria-label="Business card front">
      <h1 class="wordmark">The Duchess<br>of Nestware</h1>
      <div class="address-rule"></div>
      <p class="address">PO Box 58316, Marlow Flats, Auckland. New Zealand</p>
    </section>

    <section class="card card--back" aria-label="Business card back">
      <div class="brand-dot"></div>
      <h2 class="person-name">Corinne Dale-Petrakou</h2>
      <p class="tagline">Love your Home!</p>
      <p class="contact-line">info@duchessofnestware.example | www.duchessofnestware.example</p>
    </section>
  </main>
</body>
</html>
```